依頼詳細
昨年11月より発売していますが、大変好調に売れています。
この3月より、リボンタイプのポケ&ミントを追加発売するため、より一層拡販したくA3サイズのポスターを作成する運びとなりました。用途としましては、マルセリオン、青峰ツールズ、ハーバーランタンズ、ドラッグストアー、モバイルショップさんなどで販売していただく際に、今回のポスターを見て一般顧客様にこの商品の良さをわかっていただき、購入に至る という宣伝のポスターになります。 一見、ただのスマホポーチに見えてしまうのですが、裏には特殊シートを採用しておりスマホを入れたまま操作ができる というポイントを、しっかりポスターに表現して頂きたいです。
ターゲットは20代~40代の女性ですので宜しくお願いします。
記載項目
下記URLより商品をイメージをしてください。
http://www.kk-hotaru-example.jp/items/pokemint/index.html
http://www.kk-hotaru-example.jp/items/3stylecase_frill/index.html
スマホを入れたまま さわる、話せる をキーワードに。お願いします。
他にキャッチコピーを作っていただいてもいいです。 ある意味自由に表現して頂いて、この新商品を輝かせてください。

サイズ
A3
ページ数
片面
希望イメージ
シンプル 複雑
単色 カラフル
暗い 明るい
日常 高級
遊び心 厳粛
未来的 伝統的
女性的 男性的
希望する色
ピンク、オレンジ
納品ファイル
• 高解像度JPG (.jpg)
• イラストレーター形式 (.ai)
補足説明
弊社ホームページ  http://www.kk-hotaru-example.jp
お世話になります。

別モデルにて撮影致しましたので、添付ファイルを追加させていただき、

締め切り時間を延長させていただきます。

できましたら、新モデル画像の素材をメインで使っていただけると嬉しいです。

宜しくお願い致します。
■ 選んだ理由

商品の魅力にあう写真配列を自然な感じで引き出して頂き、
私もこの商品を持ちたいと感じさせてくれるデザインでしたので、
選ばせて頂きました。

商品のコンセプトイメージ一番合っていると思いました。

■ 提案者全員のお礼・コメント

今回はたくさんのご提案をいただきましてありがとうございました。
初めて依頼させていただきまして、提案が来る度、凄い楽しみに待っていました。
我々が考えていたデザイン以上の提案ばかりでしたので、色々と勉強になりました。

弊社ではいろいろと商品企画を行っていましてまた依頼させていただく事があると思いますので、
今後ともよろしくお願い致します。
この度はありがとうございました。

```html
<!DOCTYPE html>
<html lang="ja">
<head>
<meta charset="utf-8">
<title>Poke &amp; Mint ポスター</title>
<link rel="stylesheet" href="https://fonts.googleapis.com/css2?family=Montserrat:wght@600;800&family=M+PLUS+Rounded+1c:wght@500;800&family=Noto+Sans+JP:wght@400;700&display=swap">
<style>
  :root{
    --pink:#e6427c;
    --orange:#f29a1c;
    --red:#d92d3a;
    --ink:#3b3a3c;
    --paper:#ffffff;
  }
  html,body{margin:0;padding:0;overflow:hidden;background:#eee;}
  .poster{position:relative;width:849px;height:1200px;overflow:hidden;background:var(--paper);
    font-family:"Noto Sans JP",sans-serif;color:var(--ink);}
  .abs{position:absolute;margin:0;}
  .hero-photo{left:0;top:0;width:470px;height:1200px;
    background:linear-gradient(160deg,#e9e6e2 0%,#cfcac6 40%,#8d8a88 70%,#b9b4ae 100%);}
  .lead{left:14px;top:126px;font-family:"M PLUS Rounded 1c",sans-serif;font-weight:800;color:var(--pink);
    font-size:17px;line-height:1.45;}
  .title{left:455px;top:22px;font-family:"Montserrat",sans-serif;font-weight:800;font-size:54px;
    color:var(--ink);letter-spacing:-1px;white-space:nowrap;line-height:1;}
  .title-kana{left:560px;top:86px;font-family:"M PLUS Rounded 1c",sans-serif;font-weight:800;font-size:26px;color:var(--ink);}
  .mood{left:650px;top:136px;font-family:"M PLUS Rounded 1c",sans-serif;font-weight:800;font-size:20px;color:var(--pink);}
  .snap{background:linear-gradient(160deg,#e4dfda,#9b9591);}
  .badge-new{left:770px;top:170px;width:68px;height:68px;border-radius:50%;background:var(--red);color:#fff;
    font-family:"Montserrat",sans-serif;font-weight:800;font-size:13px;text-align:center;line-height:1.05;
    display:flex;align-items:center;justify-content:center;}
  .tag{background:var(--orange);color:#fff;font-size:12px;font-weight:700;padding:3px 10px;border-radius:3px;}
  .feature-word{font-family:"Montserrat",sans-serif;font-weight:800;font-size:62px;color:var(--pink);line-height:1;}
  .feature-verb{font-family:"M PLUS Rounded 1c",sans-serif;font-weight:800;font-size:28px;color:var(--pink);line-height:1.2;}
  .feature-note{font-family:"M PLUS Rounded 1c",sans-serif;font-weight:800;font-size:15px;line-height:1.4;color:var(--ink);}
  .uses{left:432px;top:768px;width:170px;padding:0;list-style:none;}
  .uses li{background:var(--orange);color:#fff;font-family:"M PLUS Rounded 1c",sans-serif;font-weight:800;
    font-size:17px;height:32px;line-height:32px;padding-left:12px;margin-bottom:5px;border-radius:3px;}
  .petal-badge{left:722px;top:792px;width:120px;height:84px;background:var(--red);border-radius:10px;color:#fff;
    font-family:"M PLUS Rounded 1c",sans-serif;font-weight:800;font-size:14px;line-height:1.35;text-align:center;
    display:flex;align-items:center;justify-content:center;}
  .arrange{left:120px;top:918px;font-family:"M PLUS Rounded 1c",sans-serif;font-weight:800;font-size:20px;color:#fff;}
  .lineup-note{left:505px;top:1050px;font-size:9px;line-height:1.4;color:var(--ink);}
  .lineup{left:505px;top:1084px;display:grid;grid-template-columns:repeat(6,50px);gap:6px;}
  .swatch{height:50px;border-radius:6px;}
  .brand{left:20px;top:1128px;display:flex;align-items:center;gap:8px;font-family:"Montserrat",sans-serif;
    font-weight:600;font-size:22px;color:#fff;}
  .brand-dot{width:28px;height:28px;border-radius:50%;background:var(--pink);}
  .brand-url{left:20px;top:1168px;font-size:11px;color:#fff;}
</style>
</head>
<body>
<div class="poster">
  <div class="abs hero-photo" role="img" aria-label="ストライプのワンピースの女性がリボン付きポーチを持つバッグを提げて立つ写真"></div>
  <p class="abs lead">大好評のスマホポーチに<br>リボンスタイルが仲間入り！</p>

  <h1 class="abs title">Poke &amp; Mint</h1>
  <div class="abs title-kana">ポケ＆ミント</div>
  <div class="abs mood">★わたしらしく…</div>

  <div class="abs snap" style="left:480px;top:175px;width:110px;height:205px" role="img" aria-label="ポーチを首から下げた女性の写真"></div>
  <div class="abs snap" style="left:598px;top:180px;width:80px;height:190px" role="img" aria-label="ポーチを持つ女性の写真"></div>
  <div class="abs snap" style="left:686px;top:245px;width:80px;height:150px" role="img" aria-label="ポシェットとして使う女性の写真"></div>
  <div class="abs snap" style="left:774px;top:245px;width:70px;height:150px;background:linear-gradient(160deg,#f2d3d3,#c7403f)" role="img" aria-label="赤い扉の前でポーチを持つ女性の写真"></div>
  <div class="abs badge-new">NEW!<br>RIBBON</div>

  <div class="abs tag" style="left:470px;top:412px">ポーチに入れたまま</div>
  <div class="abs feature-word" style="left:440px;top:440px">Touch</div>
  <div class="abs feature-verb" style="left:470px;top:506px">さわれる！</div>
  <div class="abs feature-note" style="left:470px;top:546px">メールOK!<br>ウエブOK!<br>そのまま操作！</div>
  <div class="abs snap" style="left:650px;top:410px;width:190px;height:170px" role="img" aria-label="ポーチ越しにスマホを操作する女性の写真"></div>

  <div class="abs snap" style="left:440px;top:636px;width:160px;height:118px" role="img" aria-label="ポーチに入れたまま通話する女性の写真"></div>
  <div class="abs tag" style="left:640px;top:600px">ポーチに入れたまま</div>
  <div class="abs feature-word" style="left:620px;top:628px">Talk</div>
  <div class="abs feature-verb" style="left:640px;top:694px">話せる！</div>
  <div class="abs feature-note" style="left:640px;top:734px">とっさの電話にも<br>そのまま通話！</div>

  <ul class="abs uses">
    <li>バッグチャーム</li>
    <li>ネックストラップ</li>
    <li>ポシェット</li>
    <li>デジカメケース</li>
  </ul>
  <div class="abs petal-badge">大人カワイイ<br>Petalも<br>好評発売中！</div>

  <div class="abs arrange">使い方いろいろ、自由にアレンジ♪</div>

  <div class="abs lineup-note">4Way スマートホンケース Petal<br>ロングストラップ＋ショートストラップ付き</div>
  <div class="abs lineup" role="img" aria-label="花型スマホポーチのカラーバリエーション写真12点">
    <div class="swatch" style="background:#2b2b2b"></div>
    <div class="swatch" style="background:#5a3a2c"></div>
    <div class="swatch" style="background:#e9e2d6"></div>
    <div class="swatch" style="background:#c9a68a"></div>
    <div class="swatch" style="background:#d4336a"></div>
    <div class="swatch" style="background:#b3262f"></div>
    <div class="swatch" style="background:#6a6f8c"></div>
    <div class="swatch" style="background:#2f3f6b"></div>
    <div class="swatch" style="background:#b79ad1"></div>
    <div class="swatch" style="background:#f2b7c8"></div>
    <div class="swatch" style="background:#f5f0e8"></div>
    <div class="swatch" style="background:#e85c8c"></div>
  </div>

  <div class="abs brand"><span class="brand-dot"></span>Hotaru</div>
  <div class="abs brand-url">http://www.kk-hotaru-example.jp</div>
</div>
</body>
</html>
```